Business Card Design Project

Need a business card designed for a horse racing/gambling centered company.
Company name is BrightQuill.com.au
Company colours are similar to those in the logo.
Something clean and modern , designer given liberty to be creative.
Incorporate the logo is preferred.
Single or Double Sided fine
Must include :
Name
Mobile Number
Email Address
Reason: Apologies, I have been traveling unexpectedly with business and just need the extra two days to reply and give feedback before making a decision.
Industry/Entity Type
Business

```html
<!DOCTYPE html>
<html lang="en">
<head>
<meta charset="utf-8">
<title>BrightQuill.com.au Business Card</title>
<link rel="stylesheet" href="https://fonts.googleapis.com/css2?family=Bebas+Neue&family=Arimo:wght@400;700&display=swap">
<style>
  :root {
    --page-bg: #e9eeee;
    --front-dark: #1e2731;
    --front-light: #4b6787;
    --card-white: #ffffff;
    --slate: #4f6e8d;
    --brand-green: #2fcf86;
    --divider: #3a3a3a;
    --text-light: #ffffff;
  }
  * { margin: 0; padding: 0; box-sizing: border-box; }
  html, body { width: 1200px; height: 900px; overflow: hidden; }
  body { background: var(--page-bg); position: relative; font-family: "Arimo", Arial, sans-serif; }

  .card {
    position: absolute;
    top: 265px;
    width: 514px;
    height: 292px;
    border-radius: 12px;
  }
  .card-front {
    left: 73px;
    background: linear-gradient(135deg, var(--front-dark) 0%, #2f3f51 45%, var(--front-light) 100%);
    display: flex;
    align-items: center;
    justify-content: center;
    gap: 14px;
  }
  .brand-dot {
    width: 30px;
    height: 30px;
    border-radius: 50%;
    background: var(--brand-green);
  }
  .brand-name {
    font-family: "Bebas Neue", Impact, sans-serif;
    font-size: 44px;
    letter-spacing: 1px;
    color: var(--brand-green);
    line-height: 1;
  }

  .card-back { left: 612px; background: var(--card-white); }
  .person-name {
    position: absolute;
    left: 74px;
    top: 104px;
    font-family: "Bebas Neue", Impact, sans-serif;
    font-weight: 400;
    font-size: 51px;
    line-height: 40px;
    color: var(--slate);
    letter-spacing: 0.3px;
    white-space: nowrap;
  }
  .divider {
    position: absolute;
    left: 207px;
    top: 108px;
    height: 76px;
    border-left: 2px dotted var(--divider);
  }
  .contact-list {
    position: absolute;
    left: 226px;
    top: 108px;
    list-style: none;
    display: flex;
    flex-direction: column;
    gap: 12px;
  }
  .contact-item {
    width: 218px;
    height: 17px;
    background: var(--slate);
    color: var(--text-light);
    font-size: 14px;
    line-height: 17px;
    padding-left: 5px;
    white-space: nowrap;
    overflow: hidden;
  }
</style>
</head>
<body>
  <section class="card card-front">
    <span class="brand-dot"></span>
    <span class="brand-name">BrightQuill.com.au</span>
  </section>

  <section class="card card-back">
    <h1 class="person-name">Owen<br>Tarrick</h1>
    <span class="divider"></span>
    <ul class="contact-list">
      <li class="contact-item">+(041) 555 0182</li>
      <li class="contact-item">Owen@brightquill.com.au</li>
      <li class="contact-item">www.brightquill.com.au</li>
    </ul>
  </section>
</body>
</html>
```